Business Card Design

redesign of card and recreation of logo based on image provided. the business is located in new york so the Halvard Bridge figures prominently in the scheme. product should be very clean.

Industry/Entity Type

Real Estate

Contact Information for Business Card

Owen Tillbury 318 Dellmont Avenue Brooklyn, New York 11238 owen@otrkhome.com Mobile: 646-555-0193

Colors
cadf82
1b1b1b
ffffff

Requirements
Nice to have
• Halvard Bridge

```html
<!DOCTYPE html>
<html lang="en">
<head>
<meta charset="utf-8">
<title>Tillbury &amp; Assoc. — Business Card</title>
<link href="https://fonts.googleapis.com/css2?family=Cormorant+Garamond:wght@500&family=Lato:wght@400;700&display=swap" rel="stylesheet">
<style>
  :root {
    --ink: #1b1b1b;
    --ink-soft: #2e2e2e;
    --paper: #ffffff;
    --backdrop: #d9d9d9;
    --band: #3a3a3a;
    --band-text: #f2f2f2;
    --art-light: #ececec;
    --art-mid: #c4c4c4;
    --art-deep: #a9a9a9;
  }
  * { margin: 0; padding: 0; box-sizing: border-box; }
  html, body { width: 1200px; height: 900px; overflow: hidden; }
  body {
    background: var(--backdrop);
    display: flex;
    flex-direction: column;
    align-items: center;
    justify-content: center;
    gap: 40px;
  }
  .card {
    position: relative;
    width: 660px;
    height: 377px;
    overflow: hidden;
    box-shadow: 0 6px 18px rgba(0,0,0,0.25);
  }
  .firm-name {
    font-family: "Lato", Arial, sans-serif;
    font-weight: 400;
    line-height: 1;
    text-align: center;
  }

  /* Back */
  .card--back {
    background: linear-gradient(160deg, #3a3a3a 0%, var(--ink) 55%, #111 100%);
  }
  .card--back .firm-name {
    position: absolute;
    left: 0; right: 0; top: 130px;
    font-size: 38px;
    color: var(--paper);
  }
  .back-rule {
    position: absolute;
    left: 80px; right: 0; bottom: 62px;
    height: 4px;
    background: var(--paper);
  }

  /* Front */
  .card--front { background: var(--paper); }
  .bridge-art {
    position: absolute;
    left: 0; top: 80px;
    width: 500px; height: 240px;
    background:
      radial-gradient(ellipse 60% 70% at 45% 65%, var(--art-deep) 0%, var(--art-mid) 45%, rgba(255,255,255,0) 100%),
      linear-gradient(90deg, var(--art-light) 0%, rgba(255,255,255,0) 100%);
    -webkit-mask-image: linear-gradient(90deg, rgba(0,0,0,0.5) 0%, #000 25%, #000 70%, transparent 100%);
    mask-image: linear-gradient(90deg, rgba(0,0,0,0.5) 0%, #000 25%, #000 70%, transparent 100%);
    opacity: 0.75;
  }
  .card--front .firm-name {
    position: absolute;
    right: 30px; top: 42px;
    width: 300px;
    font-size: 26px;
    color: var(--ink-soft);
  }
  .holder {
    position: absolute;
    right: 30px; top: 112px;
    width: 300px;
    text-align: center;
    color: var(--ink-soft);
  }
  .holder__name {
    font-family: "Cormorant Garamond", Georgia, serif;
    font-weight: 500;
    font-size: 19px;
    text-transform: uppercase;
  }
  .holder__role {
    font-family: "Lato", Arial, sans-serif;
    font-size: 8px;
    font-weight: 700;
    letter-spacing: 1px;
    text-transform: uppercase;
    margin-top: 2px;
  }
  .contact-band {
    position: absolute;
    left: 24px; right: 24px; bottom: 22px;
    height: 62px;
    background: linear-gradient(180deg, #4a4a4a, var(--band));
    display: flex;
    align-items: center;
    justify-content: space-between;
    padding: 0 22px;
    color: var(--band-text);
    font-family: "Lato", Arial, sans-serif;
    font-size: 12px;
    line-height: 1.35;
  }
  .contact-item { display: flex; align-items: center; gap: 12px; }
  .contact-item svg { width: 18px; height: 18px; fill: none; stroke: var(--band-text); stroke-width: 1.6; flex: none; }
</style>
</head>
<body>

<section class="card card--back" aria-label="Card back">
  <div class="firm-name">Tillbury &amp; Assoc.</div>
  <div class="back-rule"></div>
</section>

<section class="card card--front" aria-label="Card front">
  <div class="bridge-art" role="img" aria-label="Drawing of the Halvard Bridge with the New York skyline"></div>

  <div class="firm-name">Tillbury &amp; Assoc.</div>

  <div class="holder">
    <div class="holder__name">Owen Tillbury</div>
    <div class="holder__role">Broker</div>
  </div>

  <div class="contact-band">
    <div class="contact-item">
      <svg viewBox="0 0 24 24" aria-hidden="true"><path d="M3 11 12 3l9 8"/><path d="M6 10v10h12V10"/><path d="M10 20v-6h4v6"/></svg>
      <div>318 Dellmont Avenue<br>Brooklyn, New York 11238</div>
    </div>
    <div class="contact-item">
      <svg viewBox="0 0 24 24" aria-hidden="true"><path d="M5 3h4l2 5-3 2a11 11 0 0 0 6 6l2-3 5 2v4a2 2 0 0 1-2 2A17 17 0 0 1 3 5a2 2 0 0 1 2-2z"/></svg>
      <div>T: 646-555-0193<br>F: 646-555-0178</div>
    </div>
    <div class="contact-item">
      <svg viewBox="0 0 24 24" aria-hidden="true"><circle cx="12" cy="12" r="9"/><path d="M3 12h18M12 3c3 3 3 15 0 18M12 3c-3 3-3 15 0 18"/></svg>
      <div>owen@otrkhome.com<br>www.otrkhome.com</div>
    </div>
  </div>
</section>

</body>
</html>
```